A.I. Software PowerPoint Presentation

We need a PowerPoint presentation design for our artificial intelligence product qvPilot.

We've attached our current PowerPoint to use as a base. This presentation is used to introduce and describe what the product is, how it works, why you need it, what makes it better than other solutions, and how to implement it.

We would like the PowerPoint design to be more professional-looking as we present to executives and CIOs of banks, government, and other large corporations. We are a tech startup and would like the design to convey the feel of innovation and high-tech, but also trustworthy, reputable, and capable, for the more conservative audiences.

The PowerPoint should have minimal use of animation (animate only if necessary). It should be modern and clean and not too busy.

We appreciate design work on all of the following: slide backgrounds, title slide, fonts, pictures used in the slides, layout, charts, graphics, comparison versus, etc. If you have any ideas for the slide contents, please also provide any suggestions/recommendations.

I've also attached our qvPilot logo if that is needed, as well as our brochure.

We look forward to your submissions!

EDIT:
I would like to add that we are using PowerPoint 2010 on a PC (.pptx file), and that the slides should be in 16:9 mainly but also with 4:3 version (if possible cut off the sides and squish in the content a little, no need to make a new set of slides) as sometimes we cannot control whose projector we are presenting on. Thanks

Target Market(s)

Enterprise clients, multi-national corporations,
banks, airlines, telecommunications, government

Industry/Entity Type

Software

Font styles to use
Serif
Sans Serif

Colors

Designer to choose colors to be used in the design.

Requirements
Nice to have
• Professional, clean-look, modern design
Should not have
• Should not look cheesy (i.e. tons of stock photos, business cliche pictures)
• Should not look over-done/over-the-top
• Should not look outdated

```html
<!DOCTYPE html>
<html lang="en">
<head>
<meta charset="utf-8">
<title>Introducing qvPilot – Notes Page</title>
<link rel="stylesheet" href="https://fonts.googleapis.com/css2?family=Arimo:wght@400;700&display=swap">
<style>
  :root {
    --navy: #1f5fa6;
    --cyan: #2ab4e6;
    --teal: #45b8ae;
    --grey-text: #8a8a8a;
    --ink: #111111;
    --rule: #d4d4d4;
    --frame: #1a1a1a;
    --photo-light: #e9ecef;
    --photo-dark: #8d949b;
    --paper: #ffffff;
  }
  * { box-sizing: border-box; margin: 0; padding: 0; }
  html, body { width: 1200px; height: 899px; overflow: hidden; background: var(--paper); }
  body { position: relative; font-family: "Arimo", Arial, sans-serif; color: var(--ink); }

  .slide {
    position: absolute; left: 10px; top: 26px; width: 897px; height: 505px;
    border: 1.5px solid var(--frame); background: var(--paper);
  }
  .slide-title {
    position: absolute; left: 46px; top: 28px; font-size: 30px; font-weight: 700;
    color: var(--navy); white-space: nowrap;
  }
  .slide-title .brand { color: var(--cyan); font-weight: 400; margin-left: 6px; }
  .slide-subtitle {
    position: absolute; left: 46px; top: 73px; font-size: 14px; color: #333;
  }

  .step { position: absolute; top: 135px; width: 182px; text-align: center; }
  .step-1 { left: 75px; }
  .step-2 { left: 355px; }
  .step-3 { left: 636px; }

  .step-photo {
    position: relative; width: 182px; height: 168px; border: 3px solid var(--navy);
    border-radius: 18px; overflow: hidden;
    background: linear-gradient(160deg, var(--photo-light) 0%, #c3c8cd 45%, var(--photo-dark) 100%);
  }
  .step-badge {
    position: absolute; left: -25px; top: -14px; width: 52px; height: 52px; border-radius: 50%;
    background: var(--navy); color: #fff; font-weight: 700; font-size: 28px;
    display: flex; align-items: center; justify-content: center; z-index: 2;
  }
  .step-caption { margin-top: 18px; line-height: 1.25; }
  .caption-grey { font-size: 14px; color: var(--grey-text); }
  .caption-brand { font-size: 26px; color: var(--cyan); line-height: 1.05; }
  .caption-blue { font-size: 14px; color: var(--navy); }
  .step-1 .caption-brand { margin-top: 10px; }
  .step-2 .caption-grey, .step-3 .caption-grey { margin-top: 12px; }

  .mode-button {
    position: absolute; top: 408px; width: 180px; height: 49px; background: var(--teal);
    color: #fff; font-size: 14px; line-height: 1.3; display: flex; align-items: center;
    justify-content: center; text-align: center; border-radius: 0 0 4px 0;
  }
  .mode-semi { left: 356px; }
  .mode-auto { left: 637px; }

  .speaker-notes {
    position: absolute; left: 24px; top: 553px; width: 880px; font-size: 16px; line-height: 20px;
  }
  .speaker-notes p { margin-bottom: 20px; }

  .notes-column { position: absolute; left: 925px; top: 46px; width: 257px; }
  .notes-label { font-size: 16px; padding-left: 10px; height: 29px; }
  .notes-line { height: 37.6px; border-top: 1px solid var(--rule); }

  .page-number { position: absolute; right: 19px; top: 860px; font-size: 16px; }
</style>
</head>
<body>
  <section class="slide">
    <h1 class="slide-title">Introducing<span class="brand">qvPilot</span></h1>
    <p class="slide-subtitle">Real World Natural Language Interaction</p>

    <div class="step step-1">
      <div class="step-badge">1</div>
      <div class="step-photo" role="img" aria-label="Photo of a live agent at a laptop beside a humanoid robot"></div>
      <div class="step-caption">
        <div class="caption-grey">Live Agent Works</div>
        <div class="caption-brand">qvPilot</div>
        <div class="caption-blue">Learns</div>
      </div>
    </div>

    <div class="step step-2">
      <div class="step-badge">2</div>
      <div class="step-photo" role="img" aria-label="Photo of a humanoid robot working with a live agent looking on"></div>
      <div class="step-caption">
        <div class="caption-brand">qvPilot</div>
        <div class="caption-blue">Works</div>
        <div class="caption-grey">Live Agent Verifies</div>
      </div>
    </div>

    <div class="step step-3">
      <div class="step-badge">3</div>
      <div class="step-photo" role="img" aria-label="Photo of a humanoid robot at a laptop with more robots behind"></div>
      <div class="step-caption">
        <div class="caption-brand">qvPilot</div>
        <div class="caption-blue">Works Independently</div>
        <div class="caption-grey">Live Agent Verifies</div>
      </div>
    </div>

    <div class="mode-button mode-semi">Semi Automated<br>Mode</div>
    <div class="mode-button mode-auto">Automated<br>Mode</div>
  </section>

  <div class="speaker-notes">
    <p>qvPilot starts by learning from real customer conversations. Train qvPilot with an initial set of conversations that live agents had previously.</p>
    <p>With this initial training as a starting point, qvPilot then learns in semi-automatic mode from “live” customer interactions by using a unique on-the-job training platform. In this semi-automatic mode, live agents can serve customers as usual while simultaneously training qvPilot with real human conversations.</p>
    <p>When ready, switch to its automatic mode, where it has the self-assessment capability to gauge its confidence and can escalate to a live agent if needed.</p>
  </div>

  <aside class="notes-column">
    <div class="notes-label">Your notes:</div>
    <div class="notes-line"></div><div class="notes-line"></div><div class="notes-line"></div>
    <div class="notes-line"></div><div class="notes-line"></div><div class="notes-line"></div>
    <div class="notes-line"></div><div class="notes-line"></div><div class="notes-line"></div>
    <div class="notes-line"></div><div class="notes-line"></div><div class="notes-line"></div>
    <div class="notes-line"></div><div class="notes-line"></div><div class="notes-line"></div>
    <div class="notes-line"></div><div class="notes-line"></div><div class="notes-line"></div>
    <div class="notes-line"></div><div class="notes-line"></div>
  </aside>

  <div class="page-number">3</div>
</body>
</html>
```